Wellspring Care Alliance Vonzo Ads

We want an ad created for the gay dating app vonzo. The size is 300x250. We want the ad to be sexy, with a shirtless man. We are advertising our free HIV and PrEP services. We are open to slogans about maybe "Bringing HIV and PrEP To You"
"Free PrEP and HIV Management"
Open to ideas.

We also offer through the Harborlight Support Fund
Copay Assistance, Insurance Premium Assistance, Free Medical Services, etc
Our website is wcanj.org

I do want the ad to have a Book Now Button

Gay sexually active males

```html
<!DOCTYPE html>
<html lang="en">
<head>
<meta charset="UTF-8">
<title>Wellspring Care Alliance – Free PrEP &amp; HIV Management</title>
<link href="https://fonts.googleapis.com/css2?family=Montserrat:wght@500;600&family=Poppins:wght@500;600;700&display=swap" rel="stylesheet">
<style>
  :root {
    --bg-dark: #1c1c1e;
    --bg-mid: #2a2a2d;
    --footer: #262628;
    --white: #ffffff;
    --blue: #4f8ff7;
    --pink: #ff4f9f;
    --orange: #ff6a0a;
    --purple: #9a4fd8;
    --grey-text: #d9d9d9;
  }
  * { margin: 0; padding: 0; box-sizing: border-box; }
  html, body {
    width: 1200px; height: 1000px; overflow: hidden;
    background: var(--bg-dark);
  }
  .ad {
    position: relative; width: 1200px; height: 1000px; overflow: hidden;
    background: radial-gradient(ellipse at 70% 40%, var(--bg-mid) 0%, var(--bg-dark) 70%);
    font-family: "Poppins", sans-serif; color: var(--white);
  }
  .hero-photo {
    position: absolute; left: 600px; top: 50px; width: 600px; height: 900px;
    background:
      radial-gradient(ellipse at 35% 45%, rgba(196,140,112,0.85) 0%, rgba(150,100,80,0.6) 30%, transparent 60%),
      radial-gradient(ellipse at 85% 50%, rgba(110,70,50,0.85) 0%, transparent 45%),
      linear-gradient(180deg, rgba(255,90,170,0.25), rgba(120,80,200,0.25));
    border-radius: 30px 0 0 0;
  }
  .brand {
    position: absolute; left: 80px; top: 92px;
    display: flex; align-items: center; gap: 22px;
  }
  .brand-dot {
    width: 110px; height: 110px; border-radius: 50%;
    background: var(--purple);
  }
  .brand-name {
    font-weight: 700; font-size: 38px; line-height: 1.1; color: var(--white);
  }
  .tagline {
    position: absolute; left: 124px; top: 258px;
    font-weight: 500; font-size: 26px; color: var(--white);
  }
  .headline { font-size: 0; }
  .headline span {
    position: absolute; left: 70px; display: block;
    font-weight: 700; line-height: 1; white-space: nowrap;
  }
  .headline .free { top: 285px; font-size: 188px; color: var(--blue); font-weight: 600; letter-spacing: 2px; }
  .headline .services { top: 437px; font-size: 100px; color: var(--pink); }
  .headline .management { top: 541px; font-size: 82px; color: var(--orange); letter-spacing: 1px; }
  .stroke {
    position: absolute; left: 38px; top: 640px; width: 690px; height: 30px;
    background: var(--white); border-radius: 16px 6px 14px 4px; opacity: 0.95;
  }
  .cta {
    position: absolute; left: 88px; top: 748px; width: 443px; height: 76px;
    background: linear-gradient(90deg, var(--blue), var(--pink));
    display: flex; align-items: center; justify-content: center;
    font-family: "Montserrat", sans-serif; font-weight: 600;
    font-size: 28px; letter-spacing: 6px; color: var(--white);
  }
  .footer {
    position: absolute; left: 0; bottom: 0; width: 1200px; height: 54px;
    background: var(--footer);
    display: flex; align-items: center; padding-left: 134px; gap: 22px;
  }
  .footer-url {
    font-family: "Montserrat", sans-serif; font-weight: 500;
    font-size: 20px; letter-spacing: 5px; color: var(--grey-text);
  }
</style>
</head>
<body>
  <main class="ad">
    <div class="hero-photo" role="img" aria-label="Two shirtless young men in grey boxer briefs posing against a dark backdrop with neon pink outlines"></div>

    <div class="brand">
      <div class="brand-dot"></div>
      <div class="brand-name">Wellspring<br>Care Alliance</div>
    </div>

    <p class="tagline">Bringing HIV and PrEP To You</p>

    <h1 class="headline">
      <span class="free">FREE</span>
      <span class="services">PrEP &amp; HIV</span>
      <span class="management">MANAGEMENT</span>
    </h1>

    <div class="stroke"></div>

    <div class="cta">BOOK NOW</div>

    <footer class="footer">
      <svg width="30" height="30" viewBox="0 0 30 30" aria-hidden="true">
        <g fill="none" stroke="#e0443a" stroke-width="2">
          <circle cx="15" cy="15" r="12"/>
          <ellipse cx="15" cy="15" rx="5.5" ry="12"/>
          <line x1="3" y1="15" x2="27" y2="15"/>
          <path d="M5 9 H25 M5 21 H25"/>
        </g>
      </svg>
      <span class="footer-url">WWW. WCANJ.ORG</span>
    </footer>
  </main>
</body>
</html>
```